依頼詳細
あくまでもイメージですが、
バナーのレイアウトやイメージは添付のpdfファイルをご確認ください。

必ずしもこのレイアウトでなくてはならないわけじゃありません。
高級感を表現できるようなバナーを期待しておりますので、
レイアウト等もご提案いただければと思います。

リマーケティング広告のランディングサイトは、下記になります。
http://tsubakiyane.com/
サイトのデザインに合わせていただければ幸いです。

写真は添付したものであれば、全て使用可能です。
記載項目
①ロゴ
②「生涯最高の邸宅を…」
③外観写真(添付どれでもOKです。)
サイズ
• 300 x 250 ( ミディアムレクタングル )
• 728 x 90 ( リーダーボード )
• 468 x 60 ( フルバナー )
• 160 x 600 ( ワイドスカイスクレイパー )
• 320×50 , 320×100
希望イメージ
シンプル 複雑
単色 カラフル
暗い 明るい
日常 高級
遊び心 厳粛
未来的 伝統的
女性的 男性的
希望する色
グレー系、紫系
納品ファイル
• PNG形式 (.png)
補足説明
画像容量は全て150KB以下でお願いします。
バナーイメージを添付します。

```html
<!DOCTYPE html>
<html lang="ja">
<head>
<meta charset="utf-8">
<title>TSUBAKI YANE — 生涯最高の邸宅を</title>
<link rel="stylesheet" href="https://fonts.googleapis.com/css2?family=Noto+Serif+JP:wght@500;700&display=swap">
<style>
  :root {
    --night: #000000;
    --ink: #050507;
    --glow-white: #f4f6ff;
    --glow-blue: #5a6cff;
    --sky-top: #050a2a;
    --sky-mid: #1d3aa0;
    --house-dark: #0b0a09;
    --name: #ffffff;
  }
  html, body {
    margin: 0;
    padding: 0;
    overflow: hidden;
    background: var(--night);
  }
  .banner {
    position: relative;
    width: 1200px;
    height: 4500px;
    background: var(--night);
    overflow: hidden;
  }
  .exterior-photo {
    position: absolute;
    left: 0;
    top: 2520px;
    width: 1200px;
    height: 1680px;
    background:
      radial-gradient(ellipse 60% 18% at 50% 5%, rgba(40,70,200,0.55), transparent 70%),
      linear-gradient(180deg,
        var(--night) 0%,
        var(--sky-top) 4%,
        var(--sky-mid) 9%,
        #0c1440 15%,
        var(--house-dark) 22%,
        #1a140d 50%,
        #3a2a18 62%,
        #1c150e 80%,
        #2a2a2c 92%,
        #111 100%);
  }
  .exterior-photo::after {
    content: "";
    position: absolute;
    inset: 0;
    background:
      radial-gradient(ellipse 35% 20% at 72% 55%, rgba(200,150,80,0.35), transparent 70%),
      radial-gradient(ellipse 12% 18% at 6% 62%, rgba(220,160,90,0.45), transparent 70%);
  }
  .headline {
    position: absolute;
    top: 200px;
    left: 50%;
    transform: translateX(-50%);
    margin: 0;
    writing-mode: vertical-rl;
    font-family: "Noto Serif JP", serif;
    font-weight: 700;
    font-size: 220px;
    line-height: 1;
    letter-spacing: 58px;
    color: var(--glow-white);
    text-shadow:
      0 0 10px var(--glow-blue),
      0 0 26px var(--glow-blue),
      0 0 50px rgba(90,108,255,0.7);
    white-space: nowrap;
    z-index: 2;
  }
  .headline .ellipsis {
    letter-spacing: 0;
  }
  .brand {
    position: absolute;
    left: 0;
    top: 4200px;
    width: 1200px;
    height: 300px;
    background: var(--ink);
    display: flex;
    align-items: center;
    justify-content: center;
    gap: 36px;
  }
  .brand-mark {
    width: 44px;
    height: 44px;
    background: var(--name);
  }
  .brand-name {
    margin: 0;
    font-family: "Noto Serif JP", serif;
    font-weight: 500;
    font-size: 88px;
    line-height: 1;
    letter-spacing: 10px;
    color: var(--name);
    white-space: nowrap;
  }
</style>
</head>
<body>
  <main class="banner">
    <div class="exterior-photo" role="img" aria-label="夜にライトアップされた邸宅の外観写真"></div>
    <h1 class="headline">生涯最高の邸宅を<span class="ellipsis">・・・</span></h1>
    <footer class="brand">
      <div class="brand-mark"></div>
      <p class="brand-name">TSUBAKI YANE</p>
    </footer>
  </main>
</body>
</html>
```